Storefront Sign Design for Rental Company

8ft x 8ft sign for the road in front of my business. I need something simple and clean but professional
Updates

Need extra days to review

Target Market(s)

Potential renters

Industry/Entity Type

Car Rental

Font styles to use
Serif
Sans Serif

Requirements
Must have
• Logo
• 555-207-1968
• MarvaleBreezeRental.com
• or
• www.MarvaleBreezeRental.com
• or
• MARVALEBREEZERENTAL.COM
• whichever looks better
Nice to have
• There is many cars that drive by each day so I would like something that shows my logo, phone number, and website

```html
<!DOCTYPE html>
<html lang="en">
<head>
<meta charset="utf-8">
<title>Marvale Breeze Rental – Road Sign</title>
<link href="https://fonts.googleapis.com/css2?family=Montserrat:wght@500;700;800&display=swap" rel="stylesheet">
<style>
  :root {
    --backdrop: #e9ebee;
    --sign: #ffffff;
    --ink: #231f20;
    --rule: #2b2b2b;
  }
  * { margin: 0; padding: 0; box-sizing: border-box; }
  html, body {
    width: 1200px;
    height: 900px;
    overflow: hidden;
    background: var(--backdrop);
  }
  .canvas {
    width: 1200px;
    height: 900px;
    display: flex;
    align-items: center;
    justify-content: center;
  }
  .sign {
    width: 840px;
    height: 840px;
    background: var(--sign);
    box-shadow: 0 4px 18px rgba(0,0,0,0.12);
    position: relative;
    font-family: "Montserrat", sans-serif;
    color: var(--ink);
  }
  .brand {
    position: absolute;
    top: 110px;
    left: 0;
    right: 0;
    display: flex;
    flex-direction: column;
    align-items: center;
  }
  .brand-mark {
    width: 96px;
    height: 96px;
    background: var(--ink);
    margin-bottom: 34px;
  }
  .brand-name {
    font-weight: 800;
    color: var(--ink);
    text-transform: uppercase;
    text-align: center;
    line-height: 1;
  }
  .brand-name .line-top {
    display: block;
    font-size: 26px;
    letter-spacing: 14px;
    margin-bottom: 10px;
  }
  .brand-name .line-main {
    display: block;
    font-size: 78px;
    letter-spacing: 2px;
  }
  .brand-name .line-sub {
    display: block;
    font-size: 24px;
    letter-spacing: 16px;
    margin-top: 12px;
  }
  .contact {
    position: absolute;
    top: 470px;
    left: 0;
    right: 0;
  }
  .phone-row {
    display: flex;
    align-items: center;
    gap: 24px;
  }
  .phone-row .rule {
    flex: 1;
    height: 4px;
    background: var(--rule);
  }
  .phone {
    font-weight: 800;
    font-size: 64px;
    letter-spacing: 1px;
  }
  .website {
    margin-top: 22px;
    text-align: center;
    font-weight: 700;
    font-size: 30px;
    letter-spacing: 2px;
  }
  .website .tld {
    font-weight: 500;
    text-transform: lowercase;
  }
</style>
</head>
<body>
  <main class="canvas">
    <section class="sign">
      <div class="brand">
        <div class="brand-mark"></div>
        <div class="brand-name">
          <span class="line-top">Marvale</span>
          <span class="line-main">Breeze</span>
          <span class="line-sub">Rental</span>
        </div>
      </div>
      <div class="contact">
        <div class="phone-row">
          <span class="rule"></span>
          <span class="phone">555-207-1968</span>
          <span class="rule"></span>
        </div>
        <p class="website">WWW.MARVALEBREEZERENTAL<span class="tld">.com</span></p>
      </div>
    </section>
  </main>
</body>
</html>
```